Website Wordpress Responsive Design and Development - Landscape Company

Site is currently under construction, but the old site needs a refresh.
Need a fully responsive wordpress website (built in Elementor or comparable theme).
Here's the way it looked prior :
https://pastpages.example/snap/20220330041341/http://brookmoorgreens.example/
Their current designer came up with a website sample and it looks terrible :
https://talkowenpics.sitebuild.example/mysite/projects
Websites the client likes for some inspiration, but needs better than these :
https://www.quarrinbeckgroundworkers.example/
http://kvatelierpx.example/
https://tullidgepartners.example/
https://www.garbettcoinc.example/

Navigation includes :
• Home
• Complete structure of website content is available in the home page, yielding main information on services.
• Visually appealing but simple to use and navigate. Subtle amount of content, but enough for search engines to be able to read up the target phrases.
• Sections on the home page include :
▪ About - Information about the company and main service focus
▪ Gallery - Imagery categorized to include lightbox style zoom.
▪ Contact - Contact details and connection information
• About
• Bannered header
• Content appropriately formatted to subject
• Gallery
• Bannered header
• Each of the albums would have their own categorized image content
• Contact
• Bannered header
• Social Media connector available on all pages (like box, feed, etc) if applicable
• Content can be updated on all pages
• Basic Optimization for SEO with title tags, meta data where applicable.
• Google Analytics and Sitemap installed. (google account will be provided)
• Google Business Listing and Search Console Accounts created

Coded - Design and coding required

1 page

• Wordpress Responsive Design

```html
<!DOCTYPE html>
<html lang="en">
<head>
<meta charset="utf-8">
<title>Brookmoor Greens — Landscape Construction &amp; Maintenance</title>
<link href="https://fonts.googleapis.com/css2?family=Signika:wght@400;600;700&family=Arimo:wght@400;700&display=swap" rel="stylesheet">
<style>
:root{
  --green:#1f8a1f;
  --green-dark:#0d5c12;
  --green-light:#e4f6df;
  --ink:#111;
  --muted:#777;
  --beige:#f1f0e8;
  --white:#fff;
  --line:#e3e3e3;
}
*{box-sizing:border-box;margin:0;padding:0}
html,body{width:1200px;height:4700px;overflow:hidden}
body{position:relative;font-family:'Arimo',Arial,sans-serif;color:var(--ink);background:var(--white)}
.abs{position:absolute}
.head{font-family:'Signika',Arial,sans-serif}
.label{font-family:'Arimo',Arial,sans-serif;font-weight:700;font-size:14px;color:var(--green);text-transform:uppercase;letter-spacing:.3px}
.photo{position:absolute}

/* hero */
.hero-photo{left:0;top:0;width:1200px;height:870px;background:linear-gradient(180deg,#5b5a52 0%,#6d6a5e 35%,#4d5541 65%,#2f3d22 100%)}
.hero-shade{left:0;top:0;width:1200px;height:870px;background:rgba(0,0,0,.35)}
.topbar{left:565px;top:0;width:330px;height:40px;background:var(--green);color:#fff;font-size:15px;display:flex;align-items:center;justify-content:center;clip-path:polygon(6% 0,100% 0,94% 100%,0 100%)}
.socials{left:921px;top:0;width:192px;height:40px;background:var(--green);display:flex}
.socials span{flex:1;border-left:1px solid rgba(255,255,255,.35);display:flex;align-items:center;justify-content:center}
.socials i{width:16px;height:16px;border-radius:50%;background:#fff;display:block}
.logo-box{left:86px;top:62px;width:264px;height:77px;background:#fff;border-radius:0 0 0 18px;display:flex;align-items:center;padding-left:24px;font-family:'Signika',sans-serif;font-weight:700;font-size:26px;color:var(--green)}
.nav-box{left:367px;top:62px;width:746px;height:77px;background:#fff;border-radius:0 18px 18px 18px;display:flex;align-items:center;justify-content:flex-end;padding-right:46px;gap:18px;font-family:'Signika',sans-serif;font-weight:600;font-size:16px}
.nav-box .dot{width:7px;height:7px;background:var(--green);transform:rotate(45deg)}
.nav-box .active{color:var(--green)}
.hero-tag{left:398px;top:286px;width:404px;height:57px;background:var(--green);color:#fff;font-size:16px;display:flex;align-items:center;justify-content:center}
.hero-title{left:100px;top:360px;width:1000px;text-align:center;color:#fff;font-weight:600;font-size:62px;line-height:74px}
.hero-btn{left:507px;top:604px;width:183px;height:64px;background:#fff;border-radius:10px 10px 10px 0;display:flex;align-items:center;justify-content:center;gap:14px;font-family:'Signika',sans-serif;font-weight:600;font-size:17px}

/* contact strip */
.strip{left:86px;top:826px;width:1027px;height:124px;background:#fff;border-radius:0 0 18px 18px;box-shadow:0 10px 30px rgba(0,0,0,.12);display:flex;align-items:center;padding:0 26px}
.strip .item{display:flex;align-items:center;gap:16px;padding-right:24px;margin-right:24px;border-right:1px solid var(--line)}
.strip .item:nth-child(3){border:none}
.strip .icon{width:58px;height:48px;border-radius:50%;background:var(--green-light);display:flex;align-items:center;justify-content:center}
.strip b{font-family:'Signika',sans-serif;font-size:19px;display:block}
.strip small{font-size:12px;color:var(--muted)}
.quote-btn{margin-left:auto;width:152px;height:52px;border-radius:10px;background:linear-gradient(90deg,var(--green-dark),var(--green));color:#fff;font-family:'Signika',sans-serif;font-weight:600;font-size:15px;display:flex;align-items:center;justify-content:center;gap:10px}

/* about */
.about-title{left:86px;top:1090px;width:300px;font-size:31px;line-height:40px;font-weight:600}
.about-art{left:86px;top:1313px;width:286px;height:283px;background:radial-gradient(circle at 50% 60%,#f0f0f0,#fff 70%);border-radius:12px}
.about-text{left:438px;width:675px;font-size:13.5px;line-height:22px;color:#666}
.dropcap{float:left;font-family:'Signika',sans-serif;font-weight:700;font-size:46px;line-height:40px;color:var(--ink);margin-right:6px}
.about-img1{left:438px;top:1220px;width:324px;height:301px;background:linear-gradient(180deg,#8d99a3 0%,#a9a49a 45%,#6f7d57 70%,#8a8780 100%)}
.about-img2{left:788px;top:1220px;width:325px;height:301px;border-radius:0 0 30px 0;background:linear-gradient(180deg,#4a5a6c 0%,#c9a35e 40%,#4f6a33 70%,#3d4f2a 100%)}
.badge{left:702px;top:1299px;width:146px;height:146px;border-radius:50%;background:var(--green);border:5px solid #fff;box-shadow:0 0 0 3px var(--green);color:#fff;text-align:center;font-family:'Signika',sans-serif;font-weight:600;font-size:16px;line-height:19px;display:flex;flex-direction:column;align-items:center;justify-content:center;gap:6px}
.about-link{left:1058px;top:1582px;font-size:13px;font-weight:700;text-decoration:underline}

/* services */
.services-bg{left:0;top:1705px;width:1200px;height:416px;background:linear-gradient(180deg,#1c2b16,#2f4a22 60%,#3b5a29)}
.services-bg::after{content:"";position:absolute;inset:0;background:rgba(0,0,0,.35)}
.services-label{left:0;top:1810px;width:1200px;text-align:center}
.services-title{left:0;top:1836px;width:1200px;text-align:center;color:#fff;font-size:32px;line-height:40px;font-weight:600}
.svc-img{top:1948px;width:325px;height:296px;border-radius:30px 30px 30px 30px}
.svc-card{top:2220px;width:256px;height:197px;background:#fff;border-radius:24px 24px 12px 12px;box-shadow:0 6px 20px rgba(0,0,0,.1);text-align:center;padding-top:36px}
.svc-card h3{font-family:'Signika',sans-serif;color:var(--green-dark);font-size:21px;font-weight:600;margin-bottom:16px}
.svc-card p{font-size:13.5px;line-height:22px;color:var(--muted);padding:0 20px}
.svc-arrow{top:2394px;width:42px;height:42px;border-radius:50%;background:var(--green-light);display:flex;align-items:center;justify-content:center}

/* gallery */
.gallery-title{left:86px;top:2578px;font-size:32px;font-weight:600}
.view-all{left:989px;top:2546px;width:124px;height:54px;border-radius:10px 10px 10px 0;background:linear-gradient(90deg,var(--green-dark),var(--green));color:#fff;font-family:'Signika',sans-serif;font-weight:600;font-size:15px;display:flex;align-items:center;justify-content:center}
.g{position:absolute}
.g-plus{left:300px;top:2727px;width:74px;height:74px;border-radius:50%;background:#fff;display:flex;align-items:center;justify-content:center}

/* quote */
.quote-photo{left:0;top:3283px;width:486px;height:630px;background:linear-gradient(180deg,#3d6b2c,#2c5a22 50%,#4f7d36)}
.quote-form{left:486px;top:3283px;width:714px;height:630px;background:var(--beige)}
.field{position:absolute;height:57px;background:#fff;border-radius:28px;font-size:14px;color:#999;padding:20px 26px}
.submit{left:544px;top:3752px;width:124px;height:53px;border-radius:10px 10px 10px 0;background:linear-gradient(90deg,var(--green-dark),var(--green));color:#fff;font-family:'Signika',sans-serif;font-weight:600;font-size:15px;display:flex;align-items:center;justify-content:center}

/* footer */
.footer-photo{left:0;top:4300px;width:1200px;height:400px;background:linear-gradient(180deg,#fff 0%,#e6ece2 25%,#8fa27c 55%,#4f7a33 80%,#5f8a3a 100%)}
.f-head{top:4018px;font-family:'Signika',sans-serif;font-weight:600;font-size:20px;color:var(--green-dark);text-decoration:underline;text-underline-offset:4px}
.f-text{font-size:13.5px;line-height:22px;color:#666}
.f-list{list-style:none;font-size:14px;color:#666}
.f-list li{height:39px;display:flex;align-items:flex-start;gap:14px}
.f-list li::before{content:"";width:7px;height:7px;border-right:2px solid #333;border-top:2px solid #333;transform:rotate(45deg);margin-top:5px}
.f-social{display:flex;gap:22px}
.f-social i{width:16px;height:16px;border-radius:50%;background:var(--green-dark);display:block}
.copy{left:0;top:4334px;width:1200px;text-align:center;font-size:14px;color:#333}
.copy-line{left:86px;top:4343px;width:1027px;height:1px;background:#d9d9d9}
</style>
</head>
<body>

<!-- hero -->
<div class="photo abs hero-photo" role="img" aria-label="Large shingled home with a manicured lawn and curving gravel driveway"></div>
<div class="abs hero-shade"></div>
<div class="abs topbar">Welcome to Brookmoor Greens !</div>
<div class="abs socials"><span><i></i></span><span><i></i></span><span><i></i></span></div>
<div class="abs logo-box">Brookmoor Greens</div>
<nav class="abs nav-box">
  <span class="active">Home</span><span class="dot"></span>
  <span>About</span><span class="dot"></span>
  <span>Services</span><span class="dot"></span>
  <span>Gallery</span><span class="dot"></span>
  <span>Contact</span>
</nav>
<div class="abs hero-tag">Top quality work and excellent customer service</div>
<h1 class="abs head hero-title">Brookmoor Greens is a full service landscape construction and maintenance company.</h1>
<div class="abs hero-btn">Contact Us
  <svg width="20" height="18" viewBox="0 0 20 18"><path d="M1 8 19 1 15 17 10 11Z" fill="#0d5c12"/><path d="M10 11 19 1" stroke="#fff" stroke-width="1.5"/></svg>
</div>

<!-- contact strip -->
<div class="abs strip">
  <div class="item">
    <div class="icon"><svg width="30" height="30" viewBox="0 0 24 24"><path d="M6 3l3 4-2 2c1 3 4 6 7 7l2-2 4 3-2 3C10 20 4 14 3 5Z" fill="none" stroke="#1f8a1f" stroke-width="1.6"/></svg></div>
    <div><b>(555) 014-2884</b><small>PHONE</small></div>
  </div>
  <div class="item">
    <div class="icon"><svg width="34" height="28" viewBox="0 0 34 28"><rect x="2" y="4" width="30" height="20" rx="2" fill="none" stroke="#1f8a1f" stroke-width="1.8"/><path d="M2 5l15 11L32 5" fill="none" stroke="#1f8a1f" stroke-width="1.8"/></svg></div>
    <div><b>dale@brookmoorgreens.example</b><small>EMAIL</small></div>
  </div>
  <div class="item">
    <div class="icon"><svg width="32" height="30" viewBox="0 0 32 30"><rect x="3" y="10" width="26" height="14" rx="2" fill="none" stroke="#1f8a1f" stroke-width="1.8"/><rect x="8" y="3" width="16" height="8" fill="none" stroke="#1f8a1f" stroke-width="1.8"/><rect x="8" y="18" width="16" height="9" fill="#fff" stroke="#1f8a1f" stroke-width="1.8"/></svg></div>
    <div><b>(555) 014-9263</b><small>FAX</small></div>
  </div>
  <div class="quote-btn">Get A Quote
    <svg width="16" height="16" viewBox="0 0 16 16"><path d="M9 2H3v12h6M7 8h8M12 5l3 3-3 3" fill="none" stroke="#fff" stroke-width="1.5"/></svg>
  </div>
</div>

<!-- about -->
<div class="abs label" style="left:86px;top:1058px">About Us</div>
<h2 class="abs head about-title">A full service landscape construction and maintenance company</h2>
<div class="abs about-art" role="img" aria-label="Light grey line illustration of trees and a drafting compass"></div>
<p class="abs about-text" style="top:1054px"><span class="dropcap">W</span>e have been servicing the community for over 20 years and in that time have established ourselves as a premier contractor in the Hamptons. We pride ourselves on quality work and excellent customer service.</p>
<p class="abs about-text" style="top:1134px">At an early age, Dale Marrow began mowing lawns for local families. As he got older, the number of lawn accounts began to grow. In 1998, Dale Marrow incorporated his small maintenance company taking it to the next level.</p>
<div class="photo abs about-img1" role="img" aria-label="Shingled estate house behind a cobblestone drive"></div>
<div class="photo abs about-img2" role="img" aria-label="Garden with chairs overlooking marsh at sunset"></div>
<div class="abs badge">
  <svg width="34" height="26" viewBox="0 0 34 26"><path d="M4 22h26M10 22c0-8 4-12 7-12s7 4 7 12M17 10V3M12 6l5-3 5 3" fill="none" stroke="#fff" stroke-width="1.6"/></svg>
  <span>20 Years<br>of Experience</span>
</div>
<p class="abs about-text" style="top:1546px">Today, Brookmoor Greens services over 200 residential, municipal, and commercial properties and works with several local builders.</p>
<div class="abs about-link">About us</div>

<!-- services -->
<div class="photo abs services-bg" role="img" aria-label="Dark green garden with lavender and shrubs"></div>
<div class="abs label services-label" style="font-weight:400">Our Services</div>
<h2 class="abs head services-title">The Best Choice For Your<br>Business.</h2>

<div class="photo abs svc-img" style="left:86px;background:linear-gradient(180deg,#b9c5cf 0%,#c9b49a 35%,#4f7a2a 60%,#6d9a3a 100%)" role="img" aria-label="Mansion with clipped hedge parterre garden"></div>
<div class="photo abs svc-img" style="left:438px;background:linear-gradient(180deg,#566270 0%,#7b7d6a 35%,#7fb04a 65%,#a8d06a 100%)" role="img" aria-label="Modern home with grass paver driveway"></div>
<div class="photo abs svc-img" style="left:788px;background:linear-gradient(180deg,#c5cdd3 0%,#8a8f84 35%,#5d7a45 65%,#7a8e62 100%)" role="img" aria-label="Flower beds along a wooden boardwalk"></div>

<div class="abs svc-card" style="left:120px"><h3>Landscaping</h3><p>Dale Marrow, President, personally oversees all projects along with Ned Calloway...</p></div>
<div class="abs svc-card" style="left:472px"><h3>Maintenance</h3><p>Brookmoor Greens maintenance crews pride themselves on professionalism and...</p></div>
<div class="abs svc-card" style="left:823px"><h3>Flowers</h3><p>Brookmoor Greens can design, install, and maintain your annual container plantings.</p></div>
<div class="abs svc-arrow" style="left:227px"><svg width="12" height="12" viewBox="0 0 12 12"><path d="M4 2l4 4-4 4" fill="none" stroke="#111" stroke-width="1.8"/></svg></div>
<div class="abs svc-arrow" style="left:579px"><svg width="12" height="12" viewBox="0 0 12 12"><path d="M4 2l4 4-4 4" fill="none" stroke="#111" stroke-width="1.8"/></svg></div>
<div class="abs svc-arrow" style="left:930px"><svg width="12" height="12" viewBox="0 0 12 12"><path d="M4 2l4 4-4 4" fill="none" stroke="#111" stroke-width="1.8"/></svg></div>

<!-- gallery -->
<div class="abs label" style="left:86px;top:2543px">Our Gallery</div>
<h2 class="abs head gallery-title">Worked We Have Done</h2>
<div class="abs view-all">View All</div>

<div class="photo g" style="left:86px;top:2637px;width:501px;height:252px;border-radius:24px 0 0 0;background:linear-gradient(180deg,#3a6e34,#2e6a2a 60%,#3f8a34)" role="img" aria-label="House and lawn under a green overlay"></div>
<div class="g g-plus"><svg width="32" height="32" viewBox="0 0 32 32"><path d="M16 2v28M2 16h28" stroke="#1f8a1f" stroke-width="2"/></svg></div>
<div class="photo g" style="left:613px;top:2637px;width:237px;height:252px;border-radius:0 0 24px 0;background:linear-gradient(180deg,#dfe4e6,#5c7a3f 45%,#b8b6a8 75%,#5e7d3c)" role="img" aria-label="Stone stepping path through a garden gate"></div>
<div class="photo g" style="left:876px;top:2637px;width:237px;height:252px;border-radius:0 0 24px 0;background:linear-gradient(180deg,#e6e9ec,#9aa0a6 40%,#6a9040 70%,#c4c4bc)" role="img" aria-label="Shingled house with front walkway"></div>
<div class="photo g" style="left:86px;top:2922px;width:237px;height:252px;border-radius:24px 0 0 0;background:linear-gradient(180deg,#8e99a4,#6e7060 45%,#5a7a3a 65%,#555 85%)" role="img" aria-label="Curving paved driveway to a house"></div>
<div class="photo g" style="left:348px;top:2922px;width:238px;height:252px;border-radius:0 0 24px 0;background:linear-gradient(180deg,#bcc5c9,#4d6a33 45%,#6b9a3c 70%,#3f3325)" role="img" aria-label="Garden beds beside a winding grass path"></div>
<div class="photo g" style="left:613px;top:2922px;width:500px;height:252px;border-radius:0 0 24px 0;background:linear-gradient(180deg,#d4d9dc,#7d6e5c 40%,#4b6a36 75%,#6a9a3c)" role="img" aria-label="Large cedar shingle house with evergreens"></div>

<!-- quote -->
<div class="photo abs quote-photo" role="img" aria-label="Soft-focus green trees and hedges"></div>
<div class="abs label" style="left:86px;top:3433px;color:#fff">Reach Out</div>
<h2 class="abs head" style="left:86px;top:3460px;color:#fff;font-size:32px;line-height:40px;font-weight:600">Get a Free Quote<br>Today.</h2>
<div class="abs quote-form"></div>
<div class="field" style="left:544px;top:3393px;width:277px">First name</div>
<div class="field" style="left:835px;top:3393px;width:278px">Last name</div>
<div class="field" style="left:544px;top:3469px;width:277px">Email</div>
<div class="field" style="left:835px;top:3469px;width:278px">Phone</div>
<div class="field" style="left:544px;top:3546px;width:569px">Address</div>
<div class="field" style="left:544px;top:3622px;width:569px;height:108px;border-radius:28px">Type your message here</div>
<div class="abs submit">Submit</div>

<!-- footer -->
<div class="photo abs footer-photo" role="img" aria-label="House across a wide green lawn, fading into white"></div>
<h4 class="abs f-head" style="left:86px">About Us</h4>
<p class="abs f-text" style="left:86px;top:4072px;width:285px">At an early age, Dale Marrow began mowing lawns for local families. As he got older, the number of lawn accounts began to grow. In 1998, Dale Marrow incorporated his small maintenance company taking it to the next level.</p>
<div class="abs f-social" style="left:86px;top:4235px"><i></i><i></i><i></i></div>

<h4 class="abs f-head" style="left:472px">Quick Links</h4>
<ul class="abs f-list" style="left:472px;top:4075px">
  <li>Home</li><li>About</li><li>Services</li><li>Gallery</li><li>Contact</li>
</ul>
<h4 class="abs f-head" style="left:679px">Solutions</h4>
<ul class="abs f-list" style="left:679px;top:4075px">
  <li>Leadereship</li><li>Terms</li><li>Privacy Policy</li><li>Licenses</li><li>Sitemap</li>
</ul>
<h4 class="abs f-head" style="left:877px">Contact Info</h4>
<div class="abs f-text" style="left:877px;top:4072px;width:240px;font-size:14px">
  <p><b style="color:#333">Address:</b> PO Box 318 Westhollow, NY 00000</p>
  <p style="margin-top:18px"><b style="color:#333">Email:</b> dale@brookmoorgreens.example</p>
  <p style="margin-top:18px"><b style="color:#333">Phone:</b> (555) 014-2884</p>
  <p style="margin-top:18px"><b style="color:#333">Fax:</b> (555) 014-9263</p>
</div>
<div class="abs copy-line"></div>
<div class="abs copy"><span style="background:#fff;padding:0 14px;position:relative">© 2020 Brookmoor Greens All rights reserved.</span></div>

</body>
</html>
```